Professional, elegant brochure for funeral home

We have a funeral home. We would like a 2 sided brochure. On one side will be 3 columns for our cremation options and on the other side would be 2-3 columns of our burial options. Would like to print it and also will be putting it on our website at www.Veltranoserves.com

Use as examples

https://www.bardwellhaven.com/pricing-and-resources/online-cremation-package-options

https://pellingtonmortuary.com/wp-content/uploads/Cremation-with-Ceremony-Plans.pdf

We only need a simple 1page (front and back brochure). Once we have decided on the designer I can provide the final content to be placed on the brochure.

Target Market(s)

We are family owned business so Something soft, inviting, personable and looks professionally done.

Industry/Entity Type

Funeral Home

Requirements
Must have
• Look professional. Easy to read
Nice to have
• Softer Muted comforting colors. No bright colors.

```html
<!DOCTYPE html>
<html lang="en">
<head>
<meta charset="utf-8">
<title>Veltrano Funeral Home — Burial and Cremation Services</title>
<link rel="stylesheet" href="https://fonts.googleapis.com/css2?family=Cinzel:wght@400;600&family=Open+Sans:wght@400;600;700&display=swap">
<style>
  :root {
    --backdrop: #d6d6d6;
    --paper: #ffffff;
    --forest-dark: #2f3a24;
    --forest-mid: #5d6b3c;
    --forest-light: #9fae72;
    --moss: #7c8a4a;
    --stream: #b9c4b0;
    --band: rgba(38, 44, 30, 0.78);
    --ink: #5a5a5a;
    --ink-soft: #7d7d7d;
    --brand-blue: #3f87b8;
    --col-blue: #bcd6ea;
    --col-green: #dde7b4;
    --col-grey: #cdcdcd;
    --white: #ffffff;
  }
  * { box-sizing: border-box; margin: 0; padding: 0; }
  html, body { width: 1200px; height: 960px; overflow: hidden; }
  body {
    background: var(--backdrop);
    font-family: "Open Sans", Arial, sans-serif;
    color: var(--ink);
    position: relative;
  }
  .flyer {
    position: absolute;
    top: 130px;
    width: 540px;
    height: 700px;
    background: var(--paper);
    box-shadow: 0 6px 18px rgba(0,0,0,0.12);
  }
  .flyer--burial { left: 40px; }
  .flyer--cremation { left: 620px; }

  .brand {
    height: 92px;
    display: flex;
    align-items: center;
    justify-content: center;
    gap: 10px;
  }
  .brand__dot {
    width: 14px; height: 14px; border-radius: 50%;
    background: var(--brand-blue);
  }
  .brand__name {
    font-family: "Cinzel", Georgia, serif;
    font-weight: 600;
    font-size: 20px;
    letter-spacing: 1px;
    color: var(--brand-blue);
  }

  .hero {
    position: relative;
    height: 130px;
    background:
      linear-gradient(180deg, rgba(47,58,36,0.25) 0%, rgba(185,196,176,0.45) 55%, rgba(47,58,36,0.55) 100%),
      linear-gradient(90deg, var(--forest-mid) 0%, var(--forest-light) 30%, var(--stream) 50%, var(--forest-light) 70%, var(--forest-dark) 100%);
  }
  .hero__band {
    position: absolute;
    left: 0; right: 0; top: 44px;
    height: 44px;
    background: var(--band);
    display: flex;
    align-items: center;
    padding-left: 38px;
  }
  .hero__title {
    font-family: "Cinzel", Georgia, serif;
    font-weight: 400;
    font-size: 30px;
    letter-spacing: 2px;
    color: var(--white);
  }

  .tagline {
    font-family: "Cinzel", Georgia, serif;
    font-size: 14px;
    letter-spacing: 0.8px;
    color: var(--ink);
    padding: 14px 28px 10px;
  }

  .options {
    margin: 0 28px;
    display: grid;
    grid-template-rows: auto 1fr;
  }
  .options--two { grid-template-columns: 1fr 1fr; height: 270px; }
  .options--three { grid-template-columns: 1fr 1fr 1fr; height: 300px; }
  .options__head {
    background: linear-gradient(90deg, var(--forest-dark), var(--forest-mid) 50%, var(--forest-dark));
    color: var(--white);
    font-family: "Cinzel", Georgia, serif;
    font-size: 11px;
    line-height: 1.3;
    text-align: center;
    padding: 10px 8px;
    min-height: 46px;
    display: flex; align-items: center; justify-content: center;
  }
  .options__body {
    font-size: 9px;
    line-height: 1.45;
    color: var(--ink-soft);
    text-align: center;
    padding: 14px 14px 12px;
    display: flex;
    flex-direction: column;
    justify-content: space-between;
  }
  .options__body--blue { background: var(--col-blue); }
  .options__body--green { background: var(--col-green); }
  .options__body--grey { background: var(--col-grey); }
  .options__body p + p { margin-top: 8px; }
  .options__list { list-style: none; margin-top: 6px; }
  .options__price { font-size: 9px; margin-top: 10px; }

  .note {
    font-size: 10px;
    line-height: 1.45;
    text-align: center;
    color: var(--ink-soft);
    padding: 10px 40px 12px;
  }

  .contact {
    position: absolute;
    left: 0; right: 0; bottom: 22px;
    height: 74px;
    background:
      linear-gradient(180deg, rgba(30,36,22,0.55), rgba(30,36,22,0.7)),
      linear-gradient(90deg, var(--forest-mid), var(--moss) 40%, var(--forest-dark));
    color: var(--white);
    text-align: center;
    display: flex; flex-direction: column; justify-content: center;
    gap: 3px;
  }
  .contact__name { font-size: 11px; font-weight: 700; }
  .contact__line { font-size: 9.5px; font-weight: 600; }
</style>
</head>
<body>

  <article class="flyer flyer--burial">
    <header class="brand">
      <span class="brand__dot"></span>
      <span class="brand__name">Veltrano Funeral Home</span>
    </header>
    <section class="hero" role="img" aria-label="Photograph of a mossy forest stream with green trees">
      <div class="hero__band"><h1 class="hero__title">Burial Services</h1></div>
    </section>
    <p class="tagline">Design your healing experience. Gather. Remember. Rejoice.</p>
    <section class="options options--two">
      <h2 class="options__head">Graveside Funeral<br>Services</h2>
      <h2 class="options__head">Committal<br>Services</h2>
      <div class="options__body options__body--blue">
        <div>
          <p>A meaningful and healing service to take place at the graveside. These services can take place outdoors or even inside a mausoleum.</p>
          <p>You can select readings, speakers and create spiritual moments. You can also include military honors, a balloon release and religious elements. Memorialization can include a full memorial, upright monument, ledger, flush bronze plate, memorial benches or private estates.</p>
        </div>
        <p class="options__price">Prices start from $0000.00</p>
      </div>
      <div class="options__body options__body--green">
        <div>
          <p>Funerals often take place at the mortuary chapel or at your place of religious worship. This is followed by a graveside service and can be a profound healing experience.</p>
          <p>Family and friends gather to commit a loved one to the earth and say final farewells together, commemorating a life and marking the end of physical closeness.</p>
        </div>
        <p class="options__price">Prices start from $0000.00</p>
      </div>
    </section>
    <p class="note">Burials are often an unexpected need, and we can handle every detail should this option make sense for you and your family. Our mission is to ease your burden.</p>
    <footer class="contact">
      <p class="contact__name">Veltrano Funeral Home</p>
      <p class="contact__line">4120 Meadow Road, Ashbury, NY 14230 Telephone: (555) 214-3180</p>
      <p class="contact__line">1865 Linden Avenue, Ashbury, NY 14215 Telephone: (555) 214-7720</p>
    </footer>
  </article>

  <article class="flyer flyer--cremation">
    <header class="brand">
      <span class="brand__dot"></span>
      <span class="brand__name">Veltrano Funeral Home</span>
    </header>
    <section class="hero" role="img" aria-label="Photograph of a mossy forest stream with green trees">
      <div class="hero__band"><h1 class="hero__title">Cremation Services</h1></div>
    </section>
    <p class="tagline">Design a Cremation as Unique as the Life Lived</p>
    <section class="options options--three">
      <h2 class="options__head">Funeral Service with<br>Cremation as<br>Final Disposition</h2>
      <h2 class="options__head">Committal<br>Services</h2>
      <h2 class="options__head">Ash<br>Scattering</h2>
      <div class="options__body options__body--blue">
        <p>A traditional funeral service with visitation and viewing, followed by cremation. Family may keep the urn at home or choose a lasting resting place.</p>
        <p class="options__price">Prices start from $0000.00</p>
      </div>
      <div class="options__body options__body--green">
        <p>Healing ceremonies that help family and friends feel a sense of closure, gathering to honor and remember a loved one before the urn is placed in its final resting place.</p>
        <p class="options__price">Prices start from $0000.00</p>
      </div>
      <div class="options__body options__body--grey">
        <div>
          <p>We can help you plan a meaningful way to say goodbye. Common options include:</p>
          <ul class="options__list">
            <li>• Scattering garden</li>
            <li>• Ocean or lake</li>
            <li>• Private property</li>
            <li>• At sea</li>
            <li>• Keepsake urns</li>
          </ul>
        </div>
        <p class="options__price">Prices start from $0000.00</p>
      </div>
    </section>
    <p class="note">With cremation, the options for a final resting place are limitless. We will guide you through the possibilities as you choose the right service for your loved one.</p>
    <footer class="contact">
      <p class="contact__name">Veltrano Funeral Home</p>
      <p class="contact__line">4120 Meadow Road, Ashbury, NY 14230 Telephone: (555) 214-3180</p>
      <p class="contact__line">1865 Linden Avenue, Ashbury, NY 14215 Telephone: (555) 214-7720</p>
    </footer>
  </article>

</body>
</html>
```